Linked In Business banner needed

The image size is 1128 px X 191 px

This is a LinkedIn Company Banner. Mora Pell Kite is the company and I have attached our logo. We are an advance staffing company that only recruits sales professionals.

```html
<!DOCTYPE html>
<html lang="en">
<head>
<meta charset="utf-8">
<title>Mora Pell Kite – Company Banner</title>
<link href="https://fonts.googleapis.com/css2?family=Montserrat:wght@400;600&display=swap" rel="stylesheet">
<style>
  :root {
    --page-bg: #c9cacf;
    --navy: #063172;
    --sky: #0a9be0;
    --white: #ffffff;
    --photo-light: #d9cbb4;
    --photo-mid: #8a8f9c;
    --photo-dark: #1f2b4a;
  }
  html, body {
    margin: 0;
    width: 1200px;
    height: 1141px;
    overflow: hidden;
    background: var(--page-bg);
  }
  .company-banner {
    position: absolute;
    left: 36px;
    top: 475px;
    width: 1128px;
    height: 191px;
    background: var(--navy);
    overflow: hidden;
    box-shadow: 0 10px 22px rgba(0, 0, 0, 0.25);
  }
  .banner-shapes {
    position: absolute;
    inset: 0;
    width: 1128px;
    height: 191px;
  }
  .brand-lockup {
    position: absolute;
    left: 374px;
    top: 62px;
    width: 376px;
    font-family: "Montserrat", sans-serif;
    color: var(--white);
  }
  .brand-name {
    margin: 0;
    font-size: 38px;
    font-weight: 400;
    letter-spacing: 1px;
    text-transform: uppercase;
    line-height: 1;
    text-align: right;
    white-space: nowrap;
  }
  .brand-tagline {
    display: flex;
    align-items: center;
    gap: 6px;
    margin-top: 16px;
    font-size: 11.5px;
    font-weight: 600;
    letter-spacing: 1.6px;
    white-space: nowrap;
  }
  .brand-tagline::before {
    content: "";
    flex: 1;
    height: 1.5px;
    background: var(--white);
  }
</style>
</head>
<body>
  <section class="company-banner">
    <svg class="banner-shapes" viewBox="0 0 1128 191" aria-hidden="false">
      <defs>
        <linearGradient id="photo-tones" x1="0" y1="0" x2="1" y2="1">
          <stop offset="0" stop-color="var(--photo-light)"/>
          <stop offset="0.45" stop-color="var(--photo-mid)"/>
          <stop offset="1" stop-color="var(--photo-dark)"/>
        </linearGradient>
      </defs>
      <polygon class="accent-band" fill="var(--sky)"
        points="772,0 1128,0 1128,191 788,191 788,156 828,156 863,120 863,110 920,110 920,57 863,57 828,30 772,30"/>
      <polygon class="team-photo" role="img"
        aria-label="Photo of two business professionals in suits reviewing a tablet at a desk"
        fill="url(#photo-tones)"
        points="842,0 1128,0 1128,191 842,191 842,168 877,132 877,60 842,26"/>
    </svg>
    <div class="brand-lockup">
      <h1 class="brand-name">Mora Pell Kite</h1>
      <div class="brand-tagline">YOUR A.I. SALES RECRUITER</div>
    </div>
  </section>
</body>
</html>
```